Website for criminal defense attorney

Need a website that informs reader of my 26 years of practice, wins, practice areas (federal and capital cases, serious felonies, custody battles, etc), allows for payments (quidly app, remitro, dashu, kwiva, cards), etc. Client have referred to me as "The Iron Warden" "The Anvil" "Vanquisher". I do tend to use The Iron Warden motto and always play to win. Based in Atlanta but travel to other states. Color preferences are black and old gold, masonic themes and images (hidden), Rho Sigma Eta fraternity themes or images (likewise subtle or hidden), Spartan and warrior themes. Want strong, but not arrogant, Not about my ego, but about my ability to deliver. Have included business card, but not married to it and want to begin a brand of high end representation for remainder of my career.

```html
<!DOCTYPE html>
<html lang="en">
<head>
<meta charset="utf-8">
<title>Marcus T. Hale, LLC — Attorney at Law</title>
<link href="https://fonts.googleapis.com/css2?family=Playfair+Display:wght@500;700&family=Poppins:wght@400;500;600;700&family=Great+Vibes&family=Rubik:wght@700;900&display=swap" rel="stylesheet">
<style>
:root{
  --gold:#e3a500;
  --gold-light:#f2bd2a;
  --gold-deep:#c78c00;
  --black:#0b0b0b;
  --ink:#111111;
  --panel:#1b1b1b;
  --panel-2:#252525;
  --line:#2e2e2e;
  --text:#d9d9d9;
  --muted:#a8a8a8;
  --white:#ffffff;
}
*{box-sizing:border-box;margin:0;padding:0}
html,body{width:1200px;height:4458px;overflow:hidden;background:var(--black)}
body{position:relative;font-family:'Poppins',sans-serif;color:var(--text)}
.abs{position:absolute}
.script{font-family:'Great Vibes',cursive;color:var(--gold);font-weight:400}
.btn{position:absolute;display:flex;align-items:center;justify-content:center;background:linear-gradient(180deg,var(--gold-light),var(--gold-deep));color:var(--white);font-weight:700;text-transform:uppercase;border-radius:3px;white-space:nowrap}

/* header */
.site-header{left:0;top:0;width:1200px;height:145px;background:#121212}
.logo-mark{left:97px;top:28px;width:98px;height:98px;border:3px solid var(--gold);border-radius:50%}
.brand-name{left:222px;top:38px;font-size:33px;color:var(--gold);letter-spacing:1px;font-family:'Playfair Display',serif;font-weight:500;white-space:nowrap}
.brand-sub{left:222px;top:84px;font-size:16px;color:var(--gold);letter-spacing:.5px;white-space:nowrap}
.btn-consult{left:882px;top:31px;width:187px;height:37px;font-size:12px}
.header-phone{right:131px;top:84px;text-align:right;font-size:30px;line-height:40px;font-weight:700;color:var(--white);white-space:nowrap;letter-spacing:.5px}
.main-nav{left:0;top:145px;width:1200px;height:68px;background:#080808;display:flex;justify-content:center;gap:44px;align-items:center}
.main-nav a{font-size:14px;font-weight:600;letter-spacing:1.5px;color:var(--gold);text-decoration:none;white-space:nowrap}
.main-nav a.active{color:var(--white)}

/* hero */
.hero{left:0;top:213px;width:1200px;height:547px;background:linear-gradient(100deg,#151515 0%,#2b2b2b 45%,#4a4a4a 75%,#2a2a2a 100%)}
.hero-eyebrow{left:97px;top:362px;font-size:15px;color:var(--white);letter-spacing:.5px}
.hero-title{left:97px;top:402px;font-size:46px;line-height:56px;color:var(--white);font-family:'Playfair Display',serif;font-weight:700;letter-spacing:1px;white-space:nowrap}
.hero-title .script{font-size:66px;letter-spacing:0}
.btn-contact{left:100px;top:558px;width:187px;height:50px;font-size:17px}

/* about */
.about-photo{left:700px;top:760px;width:500px;height:662px;background:linear-gradient(160deg,#2d2d2d,#4a4a4a 50%,#1c1c1c)}
.about-name{left:130px;top:873px;font-size:35px;color:var(--white);font-family:'Playfair Display',serif;font-weight:500;letter-spacing:1px;white-space:nowrap}
.about-role{left:132px;top:910px;font-size:50px}
.about-text{left:131px;top:990px;width:455px;font-size:14.5px;line-height:27px;color:var(--text)}
.about-call{left:131px;top:1287px;font-size:13px;color:var(--text);white-space:nowrap}
.about-call b{font-size:19px;font-weight:400}
.about-rule{left:131px;top:1342px;width:463px;border-top:1px dashed #555}
.btn-profile{left:131px;top:1388px;width:156px;height:48px;font-size:17px}
.sign-mark{left:325px;top:1372px;width:75px;height:72px;background:linear-gradient(135deg,#2a2a2a,#3a3a3a);opacity:.8}
.sign-name{left:412px;top:1390px;font-size:12.5px;color:var(--gold);white-space:nowrap}
.sign-role{left:412px;top:1414px;font-size:12px;color:var(--text);white-space:nowrap}
.exp-box{left:604px;top:1104px;width:244px;height:386px;border:6px solid #3a3a3a;background:linear-gradient(180deg,#1c1c1c,#111)}
.exp-num{left:640px;top:1315px;font-family:'Rubik',sans-serif;font-weight:900;font-size:80px;color:var(--gold-light)}
.exp-label{left:642px;top:1418px;font-size:14.5px;font-weight:600;color:var(--white);letter-spacing:.5px;white-space:nowrap}
.ghost{font-family:'Rubik',sans-serif;font-weight:900;color:transparent;-webkit-text-stroke:2px #272727;letter-spacing:4px;white-space:nowrap}
.ghost-vanq{left:0;top:1475px;font-size:78px}

/* stats */
.stat{position:absolute;top:1582px;width:163px;height:123px;background:linear-gradient(180deg,var(--gold-light),var(--gold-deep));color:var(--white);text-align:center;font-weight:700;white-space:nowrap}
.stat strong{display:block;margin-top:30px;font-size:22px}
.stat span{display:block;margin-top:10px;font-size:13px;letter-spacing:.5px}

/* practice */
.sec-eyebrow{font-size:14px;color:var(--white);letter-spacing:1px;text-transform:uppercase;white-space:nowrap}
.pa-eyebrow{left:0;top:1792px;width:1200px;text-align:center}
.pa-title{left:0;top:1815px;width:1200px;text-align:center;font-size:28px;color:var(--white);font-family:'Playfair Display',serif;font-weight:500}
.pa-title .script{font-size:32px}
.pa-list{left:130px;top:1898px;width:364px}
.pa-item{position:relative;height:110px;background:var(--panel);border-bottom:1px solid #111}
.pa-item:nth-child(even){background:#242424}
.pa-num{position:absolute;left:-20px;top:35px;width:40px;height:40px;border-radius:50%;background:#2b2b2b;color:var(--muted);font-size:15px;font-weight:600;display:flex;align-items:center;justify-content:center}
.pa-item.active .pa-num{color:var(--white);background:#1a1a1a}
.pa-icon{position:absolute;left:64px;top:28px;width:62px;height:62px;background:linear-gradient(135deg,rgba(227,165,0,.35),rgba(227,165,0,.1));border-radius:4px}
.pa-name{position:absolute;left:157px;top:44px;font-family:'Playfair Display',serif;font-weight:700;font-size:17px;letter-spacing:1px;color:var(--white);white-space:nowrap}
.pa-photo{left:494px;top:1898px;width:576px;height:665px;background:linear-gradient(140deg,#8a8a8a,#3e3e3e 55%,#1f1f1f)}
.pa-card{left:520px;top:2328px;width:520px;height:222px;background:rgba(30,30,30,.88);border-radius:4px}
.pa-card h3{position:absolute;left:41px;top:38px;font-family:'Playfair Display',serif;font-size:23px;color:var(--white);letter-spacing:1px;font-weight:500}
.pa-card p{position:absolute;left:41px;top:87px;width:450px;font-size:12.5px;line-height:20px;color:var(--text)}
.pa-card a{position:absolute;left:41px;top:159px;font-size:14px;font-weight:600;color:var(--gold);letter-spacing:1px;text-decoration:none}
.ghost-warden{left:468px;top:2605px;font-size:72px}

/* testimonials */
.t-eyebrow{left:130px;top:2745px}
.t-title{left:130px;top:2767px;font-size:28px;color:var(--white);font-family:'Playfair Display',serif;font-weight:500;white-space:nowrap}
.t-title .script{font-size:32px}
.t-text{left:131px;top:2835px;width:430px;font-size:13.8px;line-height:24px;color:var(--text)}
.t-card{left:592px;top:2840px;width:476px;height:200px;background:linear-gradient(180deg,#262626,#1d1d1d);border-radius:6px}
.t-quote{left:608px;top:2845px;font-family:'Playfair Display',serif;font-size:52px;color:var(--white);font-weight:700}
.t-card-text{left:626px;top:2880px;width:425px;font-size:12.5px;line-height:22px;color:var(--text)}
.t-avatar{left:612px;top:2968px;width:42px;height:42px;border-radius:50%;background:linear-gradient(135deg,#7a6a5a,#3a3028)}
.t-name{left:672px;top:2970px;font-size:12.5px;color:var(--gold);white-space:nowrap}
.t-role{left:672px;top:2990px;font-size:12px;color:var(--white);font-weight:500}
.t-dots{left:1018px;top:3016px;display:flex;gap:5px}
.t-dots i{width:5px;height:5px;border-radius:50%;background:var(--gold);display:block}
.ghost-anvil{left:8px;top:3120px;font-size:52px;writing-mode:vertical-rl;text-orientation:upright;letter-spacing:-6px}

/* blogs */
.b-eyebrow{left:0;top:3158px;width:1200px;text-align:center}
.b-title{left:0;top:3180px;width:1200px;text-align:center;font-size:28px;color:var(--white);font-family:'Playfair Display',serif;font-weight:500}
.b-title .script{font-size:32px}
.blog-img{position:absolute;top:3260px;height:315px}
.blog-box{position:absolute;top:3508px;width:256px;height:145px;background:#0e0e0e}
.blog-box.featured{background:var(--gold-deep)}
.blog-meta{position:absolute;left:42px;top:18px;font-size:11px;color:var(--white);display:flex;gap:18px;white-space:nowrap}
.blog-head{position:absolute;left:42px;top:43px;width:200px;font-size:11.5px;line-height:21px;font-weight:500;color:var(--white)}
.blog-btn{position:absolute;left:42px;top:101px;width:96px;height:28px;font-size:11.5px;font-weight:700;display:flex;align-items:center;justify-content:center;border-radius:2px;background:var(--gold);color:var(--white);white-space:nowrap}
.blog-box.featured .blog-btn{background:var(--white);color:#111}

/* office */
.office-title{left:130px;top:3745px;font-size:38px;color:var(--white);font-family:'Playfair Display',serif;font-weight:500;white-space:nowrap}
.office-title .script{font-size:52px}
.office-phone{right:131px;top:3750px;text-align:right;font-size:36px;font-weight:700;color:var(--white);white-space:nowrap}
.office-map{left:0;top:3812px;width:1200px;height:310px;background:linear-gradient(180deg,#1e1f22,#17181a)}

/* footer */
.site-footer{left:0;top:4122px;width:1200px;height:336px;background:#111}
.f-logo{left:131px;top:4192px;width:38px;height:38px;border:2px solid var(--white);border-radius:50%}
.f-brand{left:182px;top:4198px;font-size:14px;color:var(--white);font-family:'Playfair Display',serif;white-space:nowrap}
.f-brand-sub{left:182px;top:4218px;font-size:7px;color:var(--white);white-space:nowrap}
.f-about{left:131px;top:4250px;width:240px;font-size:11px;line-height:20px;color:var(--text)}
.f-col h4{font-family:'Playfair Display',serif;font-size:18px;color:var(--white);font-weight:500;letter-spacing:1px;margin-bottom:14px;white-space:nowrap}
.f-col li{list-style:none;font-size:12px;line-height:24px;color:var(--white);text-transform:uppercase;white-space:nowrap}
.f-col li::before{content:"»";color:var(--gold);margin-right:10px}
.f-col li.on{color:var(--gold)}
.f-contact{left:855px;top:4212px;width:220px}
.f-contact p{font-size:11px;line-height:20px;color:var(--white);white-space:nowrap}
.f-contact b{color:var(--gold);font-weight:600}
.f-rule{left:131px;top:4392px;width:938px;border-top:1px solid #3a3a3a}
.f-copy{left:131px;top:4422px;font-size:12.5px;color:var(--white);white-space:nowrap}
.pay-row{right:131px;top:4416px;display:flex;align-items:center;gap:16px}
.pay{display:flex;align-items:center;gap:5px;font-size:10px;font-weight:600;color:var(--white);white-space:nowrap}
.pay i{width:12px;height:12px;background:var(--gold);display:block;border-radius:2px}
</style>
</head>
<body>

<header class="abs site-header">
  <div class="abs logo-mark"></div>
  <div class="abs brand-name">MARCUS T. HALE, LLC</div>
  <div class="abs brand-sub">ATTORNEY AT LAW</div>
  <a class="btn btn-consult">Free Consultation</a>
  <div class="abs header-phone">678-555-0142</div>
</header>
<nav class="abs main-nav">
  <a class="active">HOME</a><a>ATTORNEYS</a><a>PRACTICE AREAS</a><a>BLOG</a><a>MAKE PAYMENT</a><a>CONTACT</a>
</nav>

<section class="abs hero" role="img" aria-label="Monochrome photo of scales of justice on a courthouse desk"></section>
<div class="abs hero-eyebrow">THE MOST TALENTED LAW FIRM</div>
<h1 class="abs hero-title">RELIABLE, EXPERIENCED<br>AND <span class="script">affordable</span></h1>
<a class="btn btn-contact">Contact Now</a>

<div class="abs about-photo" role="img" aria-label="Portrait photo of the attorney in a suit, monochrome"></div>
<h2 class="abs about-name">Marcus Tobias Hale</h2>
<div class="abs about-role script">Attorney</div>
<p class="abs about-text">It is a long established fact that a reader will be distracted by the readable content of a page when looking at its layout. The point of using Lorem Ipsum is that it has a more-or-less normal distribution of letters, as opposed to using 'Content here, content here', making it look like readable English. Many desktop publishing packages and web page editors now use Lorem Ipsum as their default model text, and a search for 'lorem ipsum' will uncover many web sites still in their infancy. Various versions have evolved over the years, sometimes by accident, sometimes</p>
<div class="abs about-call">Call to ask <u>any question :</u> <b>678-555-0142</b> &nbsp;or <b>678-555-0179</b></div>
<div class="abs about-rule"></div>
<a class="btn btn-profile">View Profile</a>
<div class="abs sign-mark" role="img" aria-label="Handwritten signature"></div>
<div class="abs sign-name">MARCUS TOBIAS HALE</div>
<div class="abs sign-role">(Chairman and founder)</div>
<div class="abs exp-box" role="img" aria-label="Faint image of a statue of justice behind the experience count"></div>
<div class="abs exp-num">26</div>
<div class="abs exp-label">YEARS OF EXPERIENCE</div>
<div class="abs ghost ghost-vanq">VANQUISHER</div>

<div class="stat" style="left:178px"><strong>1234+</strong><span>COMPLETED WORKS</span></div>
<div class="stat" style="left:405px"><strong>134+</strong><span>SATISFIED CLIENTS</span></div>
<div class="stat" style="left:632px"><strong>34+</strong><span>WINNING AWARDS</span></div>
<div class="stat" style="left:859px"><strong>26+</strong><span>EXPERIENCE</span></div>

<div class="abs sec-eyebrow pa-eyebrow">Expert at</div>
<h2 class="abs pa-title">Legal <span class="script">Practice Areas</span></h2>
<div class="abs pa-list">
  <div class="pa-item"><span class="pa-num">01</span><span class="pa-icon" role="img" aria-label="Courthouse icon"></span><span class="pa-name">FEDERAL CASES</span></div>
  <div class="pa-item"><span class="pa-num">02</span><span class="pa-icon" role="img" aria-label="Money bag icon"></span><span class="pa-name">CAPITAL CASES</span></div>
  <div class="pa-item active"><span class="pa-num">03</span><span class="pa-icon" role="img" aria-label="Thief icon"></span><span class="pa-name">SERIOUS FELONIES</span></div>
  <div class="pa-item"><span class="pa-num">04</span><span class="pa-icon" role="img" aria-label="Family custody icon"></span><span class="pa-name">CUSTODY BATTLES</span></div>
  <div class="pa-item"><span class="pa-num">05</span><span class="pa-icon" role="img" aria-label="Handcuffs icon"></span><span class="pa-name">CRIMINAL LAW</span></div>
  <div class="pa-item"><span class="pa-num">06</span><span class="pa-icon" role="img" aria-label="Family icon"></span><span class="pa-name">FAMILY LAW</span></div>
</div>
<div class="abs pa-photo" role="img" aria-label="Photo of a judge's gavel beside handcuffs"></div>
<div class="abs pa-card">
  <h3>SERIOUS FELONIES</h3>
  <p>It is a long established fact that a reader will be distracted by the readable content of a page when looking at its layout. The point of using Lorem Ipsum is that it has a more-or-less normal distribution</p>
  <a>READ MORE</a>
</div>
<div class="abs ghost ghost-warden">THE IRON WARDEN</div>

<div class="abs sec-eyebrow t-eyebrow">Testimonials</div>
<h2 class="abs t-title">Our <span class="script">Happy Clients</span></h2>
<div class="abs t-text">
  <p>It is a long established fact that a reader will be distracted by the readable content of a page when looking at its layout. The point of using Lorem Ipsum is that it has a more-or-less normal distribution of letters, as opposed to using 'Content here, content here', making it look like readable English.</p>
  <p style="margin-top:24px">It is a long established fact that a reader will be distracted by the readable content of a page when looking at its layout. The point of using Lorem Ipsum is that it has a more-or-less</p>
</div>
<div class="abs t-card"></div>
<div class="abs t-quote">“</div>
<p class="abs t-card-text">It is a long established fact that a reader will be distracted by the readable content of a page when looking at its layout. The point of using Lorem Ipsum is that it has a more-or-less normal distribution</p>
<div class="abs t-avatar" role="img" aria-label="Client portrait"></div>
<div class="abs t-name">Lorna Beckett</div>
<div class="abs t-role">JUNIOR</div>
<div class="abs t-dots"><i></i><i></i><i></i></div>
<div class="abs ghost ghost-anvil">THEANVIL</div>

<div class="abs sec-eyebrow b-eyebrow">Latest Blogs</div>
<h2 class="abs b-title">Learn something more from <span class="script">Our Blogs</span></h2>

<div class="blog-img" style="left:133px;width:292px;background:linear-gradient(160deg,#bdbdbd,#3a3a3a)" role="img" aria-label="Photo of a gavel on a desk"></div>
<div class="blog-img" style="left:453px;width:295px;background:linear-gradient(160deg,#d8c6b0,#7a6a58)" role="img" aria-label="Photo of a signing hand with legal papers and scales"></div>
<div class="blog-img" style="left:774px;width:294px;background:linear-gradient(160deg,#cfcfcf,#4a4a4a)" role="img" aria-label="Photo of a lawyer reviewing a clipboard"></div>

<div class="blog-box" style="left:150px">
  <div class="blog-meta"><span>October 18, 2018</span><span>Tessa Marlow</span></div>
  <div class="blog-head">IT IS A LONG ESTABLISHED FACT THAT A READER</div>
  <div class="blog-btn">VIEW MORE</div>
</div>
<div class="blog-box featured" style="left:472px">
  <div class="blog-meta" style="color:#f7d27a"><span>October 18, 2018</span><span>Tessa Marlow</span></div>
  <div class="blog-head">IT IS A LONG ESTABLISHED FACT THAT A READER</div>
  <div class="blog-btn">VIEW MORE</div>
</div>
<div class="blog-box" style="left:793px">
  <div class="blog-meta"><span>October 18, 2018</span><span>Tessa Marlow</span></div>
  <div class="blog-head">IT IS A LONG ESTABLISHED FACT THAT A READER</div>
  <div class="blog-btn">VIEW MORE</div>
</div>

<h2 class="abs office-title">Marcus's <span class="script">Law Office</span></h2>
<div class="abs office-phone">
  <svg width="18" height="18" viewBox="0 0 24 24" style="vertical-align:middle;margin-right:6px"><path fill="#e3a500" d="M6.6 10.8a15 15 0 0 0 6.6 6.6l2.2-2.2a1 1 0 0 1 1-.25 11.4 11.4 0 0 0 3.6.57 1 1 0 0 1 1 1V20a1 1 0 0 1-1 1A17 17 0 0 1 3 4a1 1 0 0 1 1-1h3.5a1 1 0 0 1 1 1c0 1.25.2 2.45.57 3.57a1 1 0 0 1-.25 1z"/></svg>678-555-0142
</div>
<div class="abs office-map" role="img" aria-label="Dark street map showing the office location in Atlanta"></div>

<footer class="abs site-footer"></footer>
<div class="abs f-logo"></div>
<div class="abs f-brand">MARCUS T. HALE, LLC</div>
<div class="abs f-brand-sub">ATTORNEY AT LAW</div>
<p class="abs f-about">It is a long established fact that a reader will be distracted by the readable content of a page when looking at its layout. The point of using Lorem Ipsum is that it has a more-or-less normal distribution of letters, as opposed to using 'Content here, content</p>
<div class="abs f-col" style="left:417px;top:4212px">
  <h4>QUICK LINKS</h4>
  <ul><li class="on">Home</li><li>Attorneys</li><li>Blog</li><li>Make Payment</li><li>Contact Us</li></ul>
</div>
<div class="abs f-col" style="left:642px;top:4212px">
  <h4>PRACTICE AREA</h4>
  <ul><li class="on">Federal Cases</li><li>Capital Cases</li><li>Serious Felonies</li><li>Education Law</li><li>Criminal Law</li></ul>
</div>
<div class="abs f-col f-contact">
  <h4>CONTACT US</h4>
  <p>2400 Harbor Crest Avenue Suite 210<br>Atlanta,Georgia 30349<br><b>Phone:</b> 678-555-0142<br><b>Fax:</b> 678-555-0179<br><b>Email Address:</b><br>attorneymarcushale@mail.example</p>
</div>
<div class="abs f-rule"></div>
<div class="abs f-copy">© Copyright 2021 | Marcus Tobias Hale | All right reserved.</div>
<div class="abs pay-row">
  <span class="pay"><i></i>quidly app</span>
  <span class="pay"><i></i>remitro</span>
  <span class="pay"><i></i>dashu</span>
  <span class="pay"><i></i>kwiva</span>
</div>

</body>
</html>
```